Brantley Oakhollow LLC. custom built/handcrafted

I am recent small business owner looking to sell my art(drawings) and woodworking projects from my home. I have a very rough draft of a simple card design created on a simple digital program. I was hoping for a fancier lettering on the initial letters (BO). More of a calligraphy style. Also, the yellow border around the logo I would like to be a gold foil look. For it to be shiny or reflective look and to keep the other letters black with a consistent font on the card and the card white.

Target Market(s)

Local and neighboring cities

Industry/Entity Type

Art (drawing)/Woodworking

Contact Information for Business Card

My email rpoakhollow@mailbright.net, phone number 617-530-4168. In the files provided it has a yellow border around the logo and I was looking to make that a gold foil.

Font styles to use
Serif
Decorative
Script

Requirements
Nice to have
• symbols for having a Facebook and Instagram

```html
<!DOCTYPE html>
<html lang="en">
<head>
<meta charset="utf-8">
<title>Brantley Oakhollow LLC. – Business Card</title>
<link rel="stylesheet" href="https://fonts.googleapis.com/css2?family=Cinzel:wght@400;600&family=Arimo:wght@400&display=swap">
<style>
  :root {
    --backdrop: #e4e4e2;
    --card: #2a2a2a;
    --card-deep: #1f1f1f;
    --gold: #c9a24a;
    --gold-light: #ecd08a;
    --gold-soft: #b89a6a;
    --ink-light: #f2f2f2;
    --icon-fill: #d8d8d8;
  }
  * { margin: 0; padding: 0; box-sizing: border-box; }
  html, body {
    width: 1200px;
    height: 801px;
    overflow: hidden;
    background: var(--backdrop);
  }
  .canvas {
    position: relative;
    width: 1200px;
    height: 801px;
  }
  .card {
    position: absolute;
    top: 246px;
    width: 540px;
    height: 309px;
    background: radial-gradient(ellipse at 45% 40%, #333 0%, var(--card) 55%, var(--card-deep) 100%);
    box-shadow: 0 0 0 2px var(--gold-soft), 0 10px 24px rgba(0,0,0,0.18);
  }
  .card--contact { left: 40px; }
  .card--brand { left: 620px; }

  /* contact side */
  .contact-frame {
    position: absolute;
    inset: 22px;
    border: 1.5px solid var(--gold-soft);
  }
  .contact-body {
    position: absolute;
    left: 0; right: 0;
    top: 118px;
    display: flex;
    align-items: center;
    justify-content: center;
    gap: 16px;
  }
  .person {
    text-align: right;
    color: var(--ink-light);
  }
  .person-name {
    font-family: "Cinzel", serif;
    font-weight: 400;
    font-size: 19px;
    letter-spacing: 0.5px;
    line-height: 1.1;
  }
  .person-role {
    font-family: "Arimo", sans-serif;
    font-size: 15px;
    letter-spacing: 0.5px;
    margin-top: 2px;
  }
  .divider {
    width: 1px;
    height: 54px;
    background: var(--ink-light);
    opacity: 0.8;
  }
  .contact-list {
    list-style: none;
    font-family: "Arimo", sans-serif;
    font-size: 14px;
    color: var(--ink-light);
  }
  .contact-list li {
    display: flex;
    align-items: center;
    gap: 8px;
    line-height: 1.5;
  }
  .contact-icon { width: 12px; height: 12px; flex: none; }
  .social {
    position: absolute;
    left: 50%;
    bottom: 13px;
    transform: translateX(-50%);
    display: flex;
    gap: 8px;
    padding: 0 8px;
    background: var(--card);
  }
  .social-badge {
    width: 18px;
    height: 18px;
    border-radius: 4px;
    background: var(--icon-fill);
  }

  /* brand side */
  .brand-frame {
    position: absolute;
    left: 115px;
    top: 72px;
    width: 310px;
    height: 150px;
  }
  .brand-frame svg { position: absolute; inset: 0; }
  .brand-name {
    position: absolute;
    inset: 0;
    display: flex;
    align-items: center;
    justify-content: center;
    text-align: center;
    font-family: "Cinzel", serif;
    font-weight: 600;
    font-size: 24px;
    letter-spacing: 1px;
    line-height: 1.2;
    color: var(--gold);
  }
  .tagline {
    position: absolute;
    left: 0; right: 0;
    top: 234px;
    text-align: center;
    font-family: "Cinzel", serif;
    font-weight: 600;
    font-size: 12.5px;
    letter-spacing: 0.5px;
    color: var(--gold);
  }
</style>
</head>
<body>
<main class="canvas">

  <section class="card card--contact" aria-label="Contact side">
    <div class="contact-frame"></div>
    <div class="contact-body">
      <div class="person">
        <p class="person-name">Rowan P. Oakhollow</p>
        <p class="person-role">OWNER</p>
      </div>
      <div class="divider"></div>
      <ul class="contact-list">
        <li>
          <svg class="contact-icon" viewBox="0 0 24 24" aria-hidden="true">
            <path fill="#f2f2f2" d="M6.6 10.8a15 15 0 0 0 6.6 6.6l2.2-2.2c.3-.3.7-.4 1-.2 1.1.4 2.3.6 3.6.6.6 0 1 .4 1 1V20c0 .6-.4 1-1 1A17 17 0 0 1 3 4c0-.6.4-1 1-1h3.5c.6 0 1 .4 1 1 0 1.3.2 2.5.6 3.6.1.3 0 .7-.2 1z"/>
          </svg>
          <span>617-530-4168</span>
        </li>
        <li>
          <svg class="contact-icon" viewBox="0 0 24 24" aria-hidden="true">
            <rect x="2.5" y="5" width="19" height="14" fill="none" stroke="#f2f2f2" stroke-width="2"/>
            <path d="M3 6l9 7 9-7" fill="none" stroke="#f2f2f2" stroke-width="2"/>
          </svg>
          <span>rpoakhollow@mailbright.net</span>
        </li>
      </ul>
    </div>
    <div class="social" aria-label="Social profiles">
      <span class="social-badge"></span>
      <span class="social-badge"></span>
    </div>
  </section>

  <section class="card card--brand" aria-label="Brand side">
    <div class="brand-frame">
      <svg viewBox="0 0 310 150" preserveAspectRatio="none" aria-hidden="true">
        <defs>
          <linearGradient id="foil" x1="0" y1="0" x2="1" y2="1">
            <stop offset="0" stop-color="#a8782a"/>
            <stop offset="0.35" stop-color="#ecd08a"/>
            <stop offset="0.6" stop-color="#c9a24a"/>
            <stop offset="1" stop-color="#f3dc9a"/>
          </linearGradient>
        </defs>
        <rect x="1.5" y="1.5" width="307" height="147" fill="none" stroke="url(#foil)" stroke-width="2"/>
      </svg>
      <p class="brand-name">Brantley<br>Oakhollow</p>
    </div>
    <p class="tagline">CUSTOM BUILT · HANDCRAFTED</p>
  </section>

</main>
</body>
</html>
```